Driving School Business card design

Hi, we are starting a new business (Driving School) and would like your help with our business card design.
We are located in Adelaide SA.
Our aim is to help young people achieve best possible results by promoting safe and stress free driving.

Name of our school is "Velmira" which means best or most favorable.

Hope there is someone out there in wonderful world of design who can think outside of square and give us recognizable/ unique business card design.

Target Market(s)

16+

Industry/Entity Type

Business

Contact Information for Business Card

Name of our business is "Velmira driver training"
Our idea is to make letter "L' in Velmira more distinct (noticeable) by different color or font, so it gets associated with learner driver.
We like combination of white, dark gray and yellow but do not limit our self to that.
Reverse side of our card would have to incorporate writing space for date and time of the next lesson.

Requirements
Must have
• Business name: Velmira driver training
• Owner/ instructor name
• Mobile no:
• Chatterloop logo
Should not have
• Anything Not associated with driving

```html
<!DOCTYPE html>
<html lang="en">
<head>
<meta charset="utf-8">
<title>Velmira Driver Training – Business Card</title>
<link rel="stylesheet" href="https://fonts.googleapis.com/css2?family=Roboto:ital,wght@1,400;1,700;1,900&display=swap">
<style>
  :root {
    --card-white: #ffffff;
    --ink: #0a0a0a;
    --label-grey: #67726f;
    --asphalt-deep: #06121a;
    --asphalt-mid: #14232b;
  }
  html, body {
    margin: 0;
    padding: 0;
    width: 1200px;
    height: 763px;
    overflow: hidden;
    background: var(--card-white);
  }
  .card {
    position: relative;
    width: 1200px;
    height: 763px;
    background: var(--card-white);
    overflow: hidden;
    font-family: "Roboto", Arial, sans-serif;
    font-style: italic;
  }
  .road-sweep {
    position: absolute;
    inset: 0;
    width: 1200px;
    height: 763px;
  }
  .brand-name {
    position: absolute;
    left: 55px;
    top: 36px;
    margin: 0;
    font-size: 59px;
    font-weight: 700;
    letter-spacing: -0.3px;
    color: var(--ink);
    line-height: 1;
  }
  .contact-list {
    position: absolute;
    left: 56px;
    top: 168px;
    margin: 0;
  }
  .contact-label {
    margin: 0;
    font-size: 40px;
    font-weight: 400;
    color: var(--label-grey);
    line-height: 1;
  }
  .contact-value {
    margin: 14px 0 37px;
    font-size: 39px;
    font-weight: 700;
    color: var(--ink);
    line-height: 1;
  }
  .contact-value.web {
    font-size: 34px;
  }
  .social {
    position: absolute;
    right: 52px;
    bottom: 62px;
    display: flex;
    align-items: center;
    gap: 14px;
    font-size: 32px;
    font-weight: 700;
    color: var(--card-white);
  }
  .social-square {
    width: 26px;
    height: 26px;
    background: var(--card-white);
    border-radius: 4px;
  }
</style>
</head>
<body>
  <div class="card">
    <svg class="road-sweep" viewBox="0 0 1200 763" role="img" aria-label="Asphalt road photograph with curving yellow lane lines">
      <defs>
        <linearGradient id="asphalt" x1="0" y1="1" x2="1" y2="0">
          <stop offset="0" stop-color="var(--asphalt-deep)"/>
          <stop offset="1" stop-color="var(--asphalt-mid)"/>
        </linearGradient>
      </defs>
      <path d="M388 763 C 470 540, 760 300, 1200 232 L1200 763 Z" fill="url(#asphalt)"/>
    </svg>

    <h1 class="brand-name">Velmira Driver Training</h1>

    <dl class="contact-list">
      <dt class="contact-label">Owner/Instructor</dt>
      <dd class="contact-value">John Smith</dd>
      <dt class="contact-label">Mobile no</dt>
      <dd class="contact-value">000-000-000</dd>
      <dt class="contact-label">Web Adress</dt>
      <dd class="contact-value web">www.webadress.com</dd>
    </dl>

    <div class="social">
      <span class="social-square"></span>
      <span class="social-name">Chatterloop</span>
    </div>
  </div>
</body>
</html>
```